HR services to some of biggest Silicon Valley Tech companies needs a new website

We need a new website design probably 4-5 pages initially. Here are some websites we like the look of https://quintarimhub.com/ , https://www.mervoly.com/ and https://tavrine.com/ .
Updates

Slow in providing feedback

Target Market(s)

Silicon valley tech companies

Industry/Entity Type

HR

Coding

Coded - Design and coding required

Number of Pages Required

5+ page

Requirements
Nice to have
• any stock photos or images should show a diverse group of people. Our client base is very diverse

```html
<!DOCTYPE html>
<html lang="en">
<head>
<meta charset="utf-8">
<title>Kestrel HR Consulting</title>
<link href="https://fonts.googleapis.com/css2?family=Montserrat:wght@300;400;500;600;700;800&display=swap" rel="stylesheet">
<style>
:root{
  --yellow:#ffcc00;
  --ink:#1f1f1f;
  --text:#444444;
  --muted:#777777;
  --slate:#555556;
  --slate-dark:#4a4a4b;
  --white:#ffffff;
  --line:#d9d9d9;
  --paper:#f4f4f4;
}
*{box-sizing:border-box;margin:0;padding:0}
html,body{width:1200px;height:4785px;overflow:hidden}
body{position:relative;font-family:'Montserrat',sans-serif;color:var(--text);background:var(--white)}
section,header,footer{position:absolute;left:0;width:1200px}
.btn{position:absolute;display:flex;align-items:center;justify-content:center;border-radius:26px;font-size:11px;font-weight:700;letter-spacing:.3px;text-transform:uppercase}
.btn-yellow{background:var(--yellow);color:var(--ink)}
.btn-slate{background:var(--slate);color:var(--white)}
.photo{position:absolute}

/* hero */
.hero{top:0;height:598px;overflow:hidden}
.hero .photo{inset:0;background:linear-gradient(110deg,#2b2a28 0%,#4a4038 40%,#8a7a66 70%,#5a4f45 100%)}
.hero .shade{position:absolute;inset:0;background:linear-gradient(90deg,rgba(0,0,0,.55),rgba(0,0,0,.15))}
.brand{position:absolute;display:flex;align-items:center;gap:10px;font-weight:700;font-size:17px;letter-spacing:.5px}
.brand .dot{width:22px;height:22px;border-radius:50%;background:var(--yellow)}
.hero .brand{left:80px;top:36px;color:var(--white)}
.nav a{position:absolute;top:40px;font-size:13px;color:var(--white);text-decoration:none;font-weight:500}
.nav a.active{color:var(--yellow)}
.nav a.active::after{content:"";position:absolute;left:0;right:0;top:28px;height:2px;background:var(--yellow)}
.hero h1{position:absolute;left:143px;top:205px;width:700px;font-size:40px;line-height:50px;font-weight:700;color:var(--white)}
.hero h1 span{color:var(--yellow)}
.hero .lead{position:absolute;left:143px;top:316px;font-size:20px;color:var(--white);font-weight:400}
.play{position:absolute;left:350px;top:377px;width:48px;height:48px;border:2px solid var(--yellow);border-radius:50%;display:flex;align-items:center;justify-content:center}
.hero .how{position:absolute;left:425px;top:392px;color:var(--white);font-size:16px;font-weight:500}
.dots span{position:absolute;left:1103px;width:12px;height:12px;border-radius:50%;border:2px solid var(--white)}
.dots span.on{background:var(--yellow);border-color:var(--yellow)}

/* intro */
.intro{top:598px;height:643px}
.eyebrow{font-size:14px;font-weight:600;color:var(--yellow)}
.intro .eyebrow{position:absolute;left:100px;top:113px}
.intro h2{position:absolute;left:100px;top:150px;font-size:30px;line-height:40px;font-weight:700;color:var(--ink)}
.intro p{position:absolute;left:100px;top:252px;width:440px;font-size:12.5px;line-height:23.5px;color:var(--text)}
.stat{position:absolute;top:403px;width:177px;height:140px;display:flex;flex-direction:column;align-items:center;justify-content:center;color:var(--white)}
.stat b{font-size:38px;font-weight:600;line-height:44px}
.stat small{font-size:10px;font-weight:500}
.stat.years{left:100px;background:var(--slate-dark)}
.stat.years b{color:var(--yellow)}
.stat.sites{left:303px;background:var(--yellow)}
.portrait-ring{position:absolute;left:707px;top:135px;width:382px;height:382px;border-radius:50%;background:var(--yellow)}
.portrait{position:absolute;left:708px;top:150px;width:360px;height:360px;border-radius:50%;background:linear-gradient(135deg,#1f5f61 0%,#2f7776 45%,#e7e1d8 75%,#cfc3b3 100%);border:6px solid var(--white)}

/* about */
.about{top:1241px;height:563px}
.about .photo{inset:0;background:linear-gradient(100deg,#2e3134 0%,#4c4f52 35%,#6e6a63 60%,#3b3d40 100%)}
.about-panel{position:absolute;left:492px;top:191px;width:526px;height:372px;background:var(--slate)}
.about-panel .eyebrow{position:absolute;left:48px;top:35px;font-size:12px}
.about-panel h2{position:absolute;left:48px;top:60px;font-size:25px;font-weight:600;color:var(--white)}
.about-panel p{position:absolute;left:50px;width:380px;font-size:11.5px;line-height:16.5px;color:var(--white)}

/* services */
.services{top:1804px;height:647px}
.section-label{position:absolute;left:0;width:100%;text-align:center;font-size:12px;font-weight:600;color:var(--ink);letter-spacing:.5px}
.section-title{position:absolute;left:0;width:100%;text-align:center;font-size:24px;font-weight:600;color:var(--ink)}
.card{position:absolute;top:195px;width:332px;height:292px;background:var(--white);box-shadow:0 2px 12px rgba(0,0,0,.12)}
.card h3{position:absolute;left:40px;top:32px;font-size:15px;line-height:20px;font-weight:700;color:var(--ink)}
.card ul{position:absolute;left:40px;top:89px;list-style:none;width:270px}
.card li{position:relative;padding-left:18px;font-size:11.5px;line-height:23.5px;color:var(--text)}
.card li::before{content:"";position:absolute;left:2px;top:6px;width:4px;height:8px;border:solid var(--yellow);border-width:0 2px 2px 0;transform:rotate(45deg)}

/* process */
.process{top:2451px;height:561px;overflow:hidden}
.process .photo{inset:0;background:linear-gradient(100deg,#2a2826 0%,#4a4540 40%,#5d5852 65%,#33302d 100%)}
.process .shade{position:absolute;inset:0;background:rgba(0,0,0,.35)}
.process .section-title{top:99px;font-size:20px;font-weight:700;color:var(--white)}
.step{position:absolute;top:199px;width:200px;height:200px}
.step svg{position:absolute;inset:0}
.step .num{position:absolute;left:-8px;top:6px;width:46px;height:46px;border-radius:50%;background:var(--white);color:var(--ink);font-weight:700;font-size:17px;display:flex;align-items:center;justify-content:center}
.step .name{position:absolute;left:0;width:200px;top:90px;text-align:center;color:var(--white);font-weight:700;font-size:15px}

/* clients */
.clients{top:3012px;height:427px}
.clients .section-label{top:107px}
.client{position:absolute;transform:translateX(-50%);white-space:nowrap;font-size:18px;font-weight:600;color:#6f6f6f}

/* testimonial */
.testimonial{top:3439px;height:446px;background:var(--yellow)}
.testimonial blockquote{position:absolute;left:227px;top:118px;width:780px;font-size:26px;line-height:40px;font-weight:300;color:var(--ink)}
.avatar{position:absolute;left:233px;top:272px;width:70px;height:70px;border-radius:50%;background:linear-gradient(160deg,#6b4b34,#d7b39a);border:3px solid var(--white)}
.author{position:absolute;left:332px;top:289px;font-size:15px;font-weight:700;color:var(--ink)}
.role{position:absolute;left:332px;top:313px;font-size:11.5px;color:var(--ink)}
.chev{position:absolute;top:196px}

/* contact */
.contact{top:3885px;height:444px;background:var(--slate)}
.contact .section-title{top:80px;font-size:19px;font-weight:700;color:var(--white)}
.contact .sub{position:absolute;left:0;width:100%;top:110px;text-align:center;font-size:14px;color:var(--white)}
.field{position:absolute;height:48px;background:var(--white);font-size:12px;color:#8a8a8a;padding:0 24px;display:flex;align-items:center}

/* footer */
.site-footer{top:4329px;height:456px}
.site-footer .brand{left:74px;top:112px;color:var(--slate);font-size:17px}
.f-head{position:absolute;top:91px;font-size:15px;font-weight:600;color:var(--ink)}
.f-list{position:absolute;top:128px;list-style:none}
.f-list li{font-size:12px;line-height:23.3px;color:var(--text)}
.f-text{position:absolute;font-size:12px;line-height:23.3px;color:var(--text)}
.news-input{position:absolute;left:883px;top:124px;width:217px;height:28px;border-bottom:1px solid var(--line);font-size:11.5px;color:var(--text);display:flex;align-items:center;gap:8px}
.agree{position:absolute;left:883px;top:162px;font-size:11.5px;color:var(--text);display:flex;align-items:center;gap:8px}
.agree i{width:12px;height:12px;border:1px solid #aaa;display:inline-block}
.agree b{color:var(--ink);text-decoration:underline;font-weight:600}
.bottom-bar{position:absolute;left:0;top:344px;width:1200px;height:66px;background:var(--paper)}
.bottom-bar a{position:absolute;top:27px;font-size:9.5px;font-weight:600;color:var(--ink);text-decoration:none;text-transform:uppercase}
.follow{position:absolute;left:907px;top:23px;font-size:15px;font-weight:600;color:var(--ink)}
.social{position:absolute;top:26px;font-size:10.5px;font-weight:600;color:var(--slate)}
.copyright{position:absolute;left:0;width:100%;top:425px;text-align:center;font-size:10px;color:var(--text)}
.to-top{position:absolute;left:1084px;top:407px;width:40px;height:40px;border-radius:50%;background:var(--yellow);display:flex;align-items:center;justify-content:center}
</style>
</head>
<body>

<header class="hero">
  <div class="photo" role="img" aria-label="Photo of smiling colleagues working together with a tablet at a desk"></div>
  <div class="shade"></div>
  <div class="brand"><span class="dot"></span>KESTREL HR</div>
  <nav class="nav">
    <a class="active" style="left:327px">Home</a>
    <a style="left:396px">What We Do</a>
    <a style="left:507px">How It Work</a>
    <a style="left:620px">Our Clients</a>
    <a style="left:732px">About Us</a>
  </nav>
  <a class="btn btn-yellow" style="left:966px;top:24px;width:156px;height:48px;font-size:10.5px">Get in touch</a>
  <h1>Kestrel HR Consulting is the solution to all your HR issues<span>.</span></h1>
  <p class="lead">We are a one-stop-shop &nbsp;providing a variety of services</p>
  <a class="btn btn-yellow" style="left:143px;top:377px;width:175px;height:48px">Contact sales</a>
  <span class="play"><svg width="14" height="14" viewBox="0 0 14 14"><path d="M3 1 L13 7 L3 13 Z" fill="#ffffff"/></svg></span>
  <span class="how">How it Works</span>
  <div class="dots"><span class="on" style="top:317px"></span><span style="top:345px"></span><span style="top:375px"></span></div>
</header>

<section class="intro">
  <span class="eyebrow">Kestrel HR Consulting</span>
  <h2>We assess your HR needs<br>&amp; offer ongoing HR Services.</h2>
  <p>We have worked with some of the most innovative companies in Silicon Valley, across a broad range of industries, and we're proud to grow our client list every year. Kestrel's experienced professionals help implement and maintain best practices, allowing our clients to focus on their core competencies.</p>
  <div class="stat years"><b>15+</b><small>Years of Experience</small></div>
  <div class="stat sites"><b>200+</b><small>Locations Worldwide</small></div>
  <div class="portrait-ring"></div>
  <div class="portrait" role="img" aria-label="Photo of a smiling woman working at a laptop"></div>
</section>

<section class="about">
  <div class="photo" role="img" aria-label="Photo of a diverse team of professionals standing together in an office"></div>
  <div class="about-panel">
    <span class="eyebrow">WHO WE ARE</span>
    <h2>Your Human Resources Solution.</h2>
    <p style="top:103px">Kestrel HR Consulting is the solution to all your HR issues. We are a one-stop-shop providing a variety of services</p>
    <p style="top:153px">Whether you have a specific HR need or seek relief by outsourcing altogether, we have you covered</p>
    <p style="top:202px">For some clients, a Kestrel Consultant is known as the HR department and for others, we simply step in as needed on a project basis</p>
    <a class="btn btn-yellow" style="left:49px;top:277px;width:132px;height:48px">About us</a>
  </div>
</section>

<section class="services">
  <span class="section-label" style="top:100px">SOME OF OUR SERVICES</span>
  <h2 class="section-title" style="top:126px">WHAT CAN WE HELP YOU WITH?</h2>
  <article class="card" style="left:74px">
    <h3>We Help<br>Setup</h3>
    <ul>
      <li>Select and implement an HRIS system</li>
      <li>Create Company Handbook</li>
      <li>Write termination procedure</li>
      <li>Set up benefits services</li>
      <li>Set up workers comp vendor</li>
      <li>Create job descriptions for current and anticipated roles</li>
    </ul>
  </article>
  <article class="card" style="left:433px">
    <h3>Managing HR<br>Functions /Recruiting</h3>
    <ul>
      <li>Onboarding/Offboarding</li>
      <li>Employee relations</li>
      <li>Investigations</li>
      <li>Leave administration</li>
      <li>Immigration liaison</li>
      <li>Compensation management</li>
      <li>Full cycle recruitment</li>
    </ul>
  </article>
  <article class="card" style="left:793px">
    <h3>Recurring<br>Procedures</h3>
    <ul>
      <li>Review handbook annually</li>
      <li>Roll out training (required and soft skills training)</li>
      <li>Write offer letters</li>
      <li>Handle employee data and files</li>
      <li>Conduct I-9 audits</li>
      <li>Handle merit and review bonuses</li>
    </ul>
  </article>
  <a class="btn btn-slate" style="left:505px;top:526px;width:192px;height:48px">View all services</a>
</section>

<section class="process">
  <div class="photo" role="img" aria-label="Photo of a team meeting with a presenter in a modern office"></div>
  <div class="shade"></div>
  <h2 class="section-title">HOW IT WORKS</h2>
  <div class="step" style="left:71px">
    <svg viewBox="0 0 200 200"><circle cx="100" cy="100" r="96" fill="none" stroke="#ffcc00" stroke-width="3"/><circle cx="108" cy="96" r="90" fill="none" stroke="#ffcc00" stroke-width="1.5" opacity=".8"/></svg>
    <span class="num">1</span><span class="name">Discovery Call</span>
  </div>
  <div class="step" style="left:355px">
    <svg viewBox="0 0 200 200"><circle cx="100" cy="100" r="96" fill="none" stroke="#ffcc00" stroke-width="3"/><circle cx="108" cy="96" r="90" fill="none" stroke="#ffcc00" stroke-width="1.5" opacity=".8"/></svg>
    <span class="num">2</span><span class="name">Placement Process</span>
  </div>
  <div class="step" style="left:638px">
    <svg viewBox="0 0 200 200"><circle cx="100" cy="100" r="96" fill="none" stroke="#ffcc00" stroke-width="3"/><circle cx="108" cy="96" r="90" fill="none" stroke="#ffcc00" stroke-width="1.5" opacity=".8"/></svg>
    <span class="num">3</span><span class="name">Onboarding</span>
  </div>
  <div class="step" style="left:922px">
    <svg viewBox="0 0 200 200"><circle cx="100" cy="100" r="96" fill="none" stroke="#ffcc00" stroke-width="3"/><circle cx="108" cy="96" r="90" fill="none" stroke="#ffcc00" stroke-width="1.5" opacity=".8"/></svg>
    <span class="num">4</span><span class="name">Nurturing</span>
  </div>
</section>

<section class="clients">
  <span class="section-label">TRUSTED BY THOUSANDS OF COMPANIES</span>
  <span class="client" style="left:169px;top:190px">Norvale</span>
  <span class="client" style="left:323px;top:190px">Quillsoft</span>
  <span class="client" style="left:502px;top:190px">Tasklane</span>
  <span class="client" style="left:682px;top:190px">Brecon</span>
  <span class="client" style="left:860px;top:190px">Lumora</span>
  <span class="client" style="left:1022px;top:190px">Averell &amp; Co.</span>
  <span class="client" style="left:215px;top:277px">payhaven</span>
  <span class="client" style="left:394px;top:277px">kidloop</span>
  <span class="client" style="left:585px;top:277px">Hartwell Grant</span>
  <span class="client" style="left:775px;top:277px">Fenwick Rousse</span>
  <span class="client" style="left:965px;top:277px">Carrow &amp; Partners</span>
</section>

<section class="testimonial">
  <svg class="chev" style="left:72px" width="28" height="54" viewBox="0 0 28 54"><path d="M26 2 L3 27 L26 52" fill="none" stroke="#1f1f1f" stroke-width="2"/></svg>
  <blockquote>I consistently received glowing remarks about our virtual assistant from our customer base. The standard Kestrel HR Consulting upholds is premium.</blockquote>
  <div class="avatar" role="img" aria-label="Portrait photo of the client quoted"></div>
  <span class="author">DANA WHITLOW</span>
  <span class="role">Customer Service Manager, Brightframe Studio</span>
  <svg class="chev" style="left:1096px" width="28" height="54" viewBox="0 0 28 54"><path d="M2 2 L25 27 L2 52" fill="none" stroke="#1f1f1f" stroke-width="2"/></svg>
</section>

<section class="contact">
  <h2 class="section-title">LET'S START THE CONVERSATION.</h2>
  <p class="sub">Tell us what you need so you can meet your new staff.</p>
  <div class="field" style="left:117px;top:171px;width:476px">For my business</div>
  <div class="field" style="left:615px;top:171px;width:476px">Company</div>
  <div class="field" style="left:117px;top:247px;width:225px">First name</div>
  <div class="field" style="left:366px;top:247px;width:225px">Last name</div>
  <div class="field" style="left:615px;top:247px;width:225px">Email</div>
  <div class="field" style="left:864px;top:247px;width:225px">Phone</div>
  <a class="btn btn-yellow" style="left:487px;top:346px;width:225px;height:48px">Get started</a>
</section>

<footer class="site-footer">
  <div class="brand"><span class="dot"></span>KESTREL HR</div>
  <span class="f-head" style="left:373px">Company</span>
  <ul class="f-list" style="left:373px">
    <li>About Us</li><li>Our History</li><li>Contact</li><li>News &amp; Views</li><li>Board of Directors</li><li>Privacy Policy</li>
  </ul>
  <span class="f-head" style="left:602px">Address</span>
  <p class="f-text" style="left:602px;top:128px">210 Harlow Avenue, 7th Fl.<br>Fremont, CA 94538</p>
  <span class="f-head" style="left:602px;top:206px">Contact Info</span>
  <p class="f-text" style="left:602px;top:240px">Call:555-0147-2290<br>hello@kestrelhr.example</p>
  <span class="f-head" style="left:883px">Newsletter</span>
  <div class="news-input">
    <svg width="12" height="9" viewBox="0 0 12 9"><rect x=".5" y=".5" width="11" height="8" fill="none" stroke="#555" /><path d="M.5 .5 L6 5 L11.5 .5" fill="none" stroke="#555"/></svg>
    Enter Your Email Address
    <svg style="margin-left:auto" width="14" height="10" viewBox="0 0 14 10"><path d="M0 5 H12 M8 1 L12 5 L8 9" fill="none" stroke="#777"/></svg>
  </div>
  <div class="agree"><i></i>I agree to the <b>Privacy Policy.</b></div>
  <div class="bottom-bar">
    <a style="left:76px">Home</a>
    <a style="left:143px">What we do</a>
    <a style="left:234px">How it work</a>
    <a style="left:323px">Our clients</a>
    <a style="left:414px">About us</a>
    <span class="follow">Follow Us</span>
    <span class="social" style="left:1010px">Orbit</span>
    <span class="social" style="left:1044px">Relay</span>
    <span class="social" style="left:1080px">Pulse</span>
    <span class="social" style="left:1114px">Frame</span>
  </div>
  <p class="copyright">Copyright 2021 Kestrel HR Consulting</p>
  <span class="to-top"><svg width="12" height="14" viewBox="0 0 12 14"><path d="M6 13 V2 M1 6 L6 1 L11 6" fill="none" stroke="#1f1f1f" stroke-width="1.5"/></svg></span>
</footer>

</body>
</html>
```